Business Cards and Stationary for telecommunications application
BrightOak Ventures
Business Cards and Stationary for telecommunications application - Telecommunications
Creative Brief
Simple
Louis Merrow
President
20391 Kelvane Court Ashford Hollow, CO
louis@brightoakventures.com
brightoakventures.com

```html
<!DOCTYPE html>
<html lang="en">
<head>
<meta charset="utf-8">
<title>BrightOak Ventures – Business Cards</title>
<link href="https://fonts.googleapis.com/css2?family=Open+Sans:wght@400;600;700&display=swap" rel="stylesheet">
<style>
  :root {
    --page-bg: #e9e9ea;
    --card-white: #ffffff;
    --brand-red: #c8161d;
    --brand-red-light: #e02a2f;
    --brand-red-dark: #8e0c11;
    --ink-dark: #2b2b2b;
    --ink-grey: #6a6a6a;
    --swoosh: #1e1e1e;
    --text-on-red: #ffffff;
  }
  * { margin: 0; padding: 0; box-sizing: border-box; }
  html, body {
    width: 1200px; height: 874px; overflow: hidden;
    background: var(--page-bg);
    font-family: "Open Sans", Arial, sans-serif;
  }
  .canvas { position: relative; width: 1200px; height: 874px; }

  .card {
    position: absolute;
    width: 520px; height: 297px;
    border-radius: 22px;
    background: var(--card-white);
    overflow: hidden;
    box-shadow: 0 6px 18px rgba(0,0,0,0.12);
  }
  .card-back  { left: 580px; top: 110px; }
  .card-front { left: 100px; top: 470px; }
  .card svg.card-art { position: absolute; inset: 0; }

  /* Back */
  .back-brand {
    position: absolute; left: 0; right: 0; top: 112px;
    display: flex; align-items: center; justify-content: center; gap: 10px;
  }
  .brand-dot {
    width: 26px; height: 26px; border-radius: 50%;
    background: var(--brand-red);
  }
  .brand-name {
    font-weight: 600; font-size: 22px; color: var(--ink-dark);
    letter-spacing: 0.2px;
  }
  .back-web {
    position: absolute; left: 0; right: 0; top: 228px;
    text-align: center; font-size: 11px; letter-spacing: 3px;
    color: var(--ink-dark);
  }

  /* Front */
  .front-brand {
    position: absolute; left: 22px; top: 136px;
    display: flex; align-items: center; gap: 8px;
  }
  .front-brand .brand-dot { width: 22px; height: 22px; }
  .front-brand .brand-name { font-size: 15px; }

  .holder { position: absolute; left: 278px; top: 36px; color: var(--text-on-red); }
  .holder-name  { font-weight: 700; font-size: 17px; line-height: 1.2; }
  .holder-title { font-size: 12px; margin-top: 2px; }

  .contact-list {
    position: absolute; left: 278px; top: 158px;
    list-style: none; color: var(--text-on-red);
    font-size: 9.5px; line-height: 1.35;
  }
  .contact-list li { display: flex; align-items: flex-start; gap: 7px; margin-bottom: 3px; }
  .contact-icon { flex: 0 0 11px; width: 11px; height: 11px; margin-top: 1px; }
</style>
</head>
<body>
<main class="canvas">

  <section class="card card-back" aria-label="Business card back">
    <div class="back-brand">
      <span class="brand-dot"></span>
      <span class="brand-name">BrightOak Ventures</span>
    </div>
    <p class="back-web">www.brightoakventures.com</p>
  </section>

  <section class="card card-front" aria-label="Business card front">
    <svg class="card-art" viewBox="0 0 520 297" width="520" height="297" aria-hidden="true">
      <defs>
        <radialGradient id="redPanel" cx="0.55" cy="0.35" r="0.8">
          <stop offset="0" stop-color="var(--brand-red-light)"/>
          <stop offset="0.6" stop-color="var(--brand-red)"/>
          <stop offset="1" stop-color="var(--brand-red-dark)"/>
        </radialGradient>
        <linearGradient id="swooshFade" x1="0" y1="0" x2="0" y2="1">
          <stop offset="0" stop-color="#9a9a9a"/>
          <stop offset="0.5" stop-color="var(--swoosh)"/>
          <stop offset="1" stop-color="var(--swoosh)"/>
        </linearGradient>
      </defs>
      <path class="swoosh" d="M246 8 C232 90 214 210 178 297 L192 297 C222 210 240 110 256 20 Z" fill="url(#swooshFade)"/>
      <path class="red-panel" d="M300 0 H520 V297 H198 C222 220 240 130 256 55 Q268 0 300 0 Z" fill="url(#redPanel)"/>
    </svg>

    <div class="front-brand">
      <span class="brand-dot"></span>
      <span class="brand-name">BrightOak Ventures</span>
    </div>

    <div class="holder">
      <p class="holder-name">Louis Merrow</p>
      <p class="holder-title">President</p>
    </div>

    <ul class="contact-list">
      <li>
        <svg class="contact-icon" viewBox="0 0 12 12" aria-hidden="true"><circle cx="6" cy="6" r="6" fill="#fff"/><path d="M6 2.5a2.2 2.2 0 0 0-2.2 2.2C3.8 6.4 6 9.5 6 9.5s2.2-3.1 2.2-4.8A2.2 2.2 0 0 0 6 2.5z" fill="var(--brand-red)"/></svg>
        <span>20391 Kelvane Court<br>Ashford Hollow, CO</span>
      </li>
      <li>
        <svg class="contact-icon" viewBox="0 0 12 12" aria-hidden="true"><circle cx="6" cy="6" r="6" fill="#fff"/><path d="M4 3h1.3l.6 1.6-.8.6a4 4 0 0 0 1.7 1.7l.6-.8L9 6.7V8a1 1 0 0 1-1 1A5 5 0 0 1 3 4a1 1 0 0 1 1-1z" fill="var(--brand-red)"/></svg>
        <span>303.555.0148</span>
      </li>
      <li>
        <svg class="contact-icon" viewBox="0 0 12 12" aria-hidden="true"><circle cx="6" cy="6" r="6" fill="#fff"/><rect x="3" y="4" width="6" height="4.2" fill="var(--brand-red)"/><path d="M3 4l3 2.3L9 4" fill="none" stroke="#fff" stroke-width="0.7"/></svg>
        <span>louis@brightoakventures.com</span>
      </li>
      <li>
        <svg class="contact-icon" viewBox="0 0 12 12" aria-hidden="true"><circle cx="6" cy="6" r="6" fill="#fff"/><circle cx="6" cy="6" r="3" fill="none" stroke="var(--brand-red)" stroke-width="0.9"/><path d="M3 6h6M6 3c-1.3 1.8-1.3 4.2 0 6M6 3c1.3 1.8 1.3 4.2 0 6" fill="none" stroke="var(--brand-red)" stroke-width="0.7"/></svg>
        <span>www.brightoakventures.com</span>
      </li>
    </ul>
  </section>

</main>
</body>
</html>
```